The Copper Ladder

we require a classy business card design for a business coaching company that uses our current logo and the wording:

Front of card:

LOGO
Kyle Morrison
CEO
TEL: 1300 4 52918
FAX: 1300 5 52918
Mobile: 0412 638194
PO Box 917, Ferris Hollow, Brisbane, Qld 4127
e: kylem@copperladder.com.au
w: www.copperladder.com.au

Reverse side of the card:

Systematizing Businesses into Turnkey Operations
Strategic Business Plans
Sales & Marketing Programs
Sales Training & Business Coaching
Internet Marketing & Web Design

Here’s what our clients say:

“We grew from $396,000 to over $5million in 4 years and made KTS’s Rising Enterprises Roll 3 years running!” – Martin Greaves, Meridian Works

Target Market(s)

small to medium sized business owners in Australia

Industry/Entity Type

Business

Requirements
Must have
• standard business card size

```html
<!DOCTYPE html>
<html lang="en">
<head>
<meta charset="utf-8">
<title>The Copper Ladder – Business Card Options</title>
<link rel="stylesheet" href="https://fonts.googleapis.com/css2?family=Open+Sans:wght@400;700&display=swap">
<style>
  :root {
    --page: #ffffff;
    --ink: #1a1a1a;
    --ink-light: #ffffff;
    --gold-light: #ffe46b;
    --gold: #fdd022;
    --swoosh-white: #ffffff;
    --night-top: #5a5a5a;
    --night: #0d0d0d;
    --sky-light: #e4effa;
    --sky-mid: #b9d7f1;
    --sky: #4ba6e3;
    --mist-light: #d9d9d9;
    --mist: #fbfbfb;
  }
  * { margin: 0; padding: 0; box-sizing: border-box; }
  html, body {
    width: 1200px;
    height: 798px;
    overflow: hidden;
    background: var(--page);
  }
  .sheet {
    position: relative;
    width: 1200px;
    height: 798px;
  }
  .card {
    position: absolute;
    width: 432px;
    height: 250px;
    overflow: hidden;
    font-family: "Open Sans", Arial, sans-serif;
    color: var(--ink);
  }
  .card--night { left: 391px; top: 46px; color: var(--ink-light); }
  .card--sky { left: 60px; top: 477px; }
  .card--mist { left: 705px; top: 477px; }
  .card__art {
    position: absolute;
    inset: 0;
    width: 100%;
    height: 100%;
  }
  .brand {
    position: absolute;
    left: 200px;
    top: 42px;
    width: 212px;
    text-align: center;
    color: var(--ink);
    font-weight: 700;
    font-size: 23px;
    letter-spacing: -0.4px;
    line-height: 1.1;
  }
  .contact {
    position: absolute;
    left: 11px;
    top: 102px;
    font-size: 11.3px;
    line-height: 14px;
  }
  .card--sky .contact,
  .card--mist .contact { left: 13px; top: 113px; }
  .contact__name {
    font-weight: 700;
    font-size: 14px;
    line-height: 17px;
  }
  .contact__role { font-weight: 700; }
</style>
</head>
<body>
<main class="sheet">

  <section class="card card--night">
    <svg class="card__art" viewBox="0 0 432 250" preserveAspectRatio="none" aria-hidden="true">
      <defs>
        <linearGradient id="night-bg" x1="0" y1="0" x2="0.3" y2="1">
          <stop offset="0" stop-color="var(--night-top)"/>
          <stop offset="0.55" stop-color="var(--night)"/>
          <stop offset="1" stop-color="var(--night)"/>
        </linearGradient>
        <linearGradient id="gold-fill-1" x1="0" y1="0" x2="1" y2="1">
          <stop offset="0" stop-color="var(--gold-light)"/>
          <stop offset="1" stop-color="var(--gold)"/>
        </linearGradient>
      </defs>
      <rect width="432" height="250" fill="url(#night-bg)"/>
      <path d="M63 0 C80 95 220 148 432 156 L432 0 Z" fill="var(--swoosh-white)"/>
      <path d="M95 0 C112 70 230 124 432 132 L432 0 Z" fill="url(#gold-fill-1)"/>
    </svg>
    <div class="brand">The Copper Ladder</div>
    <div class="contact">
      <p class="contact__name">Kyle Morrison</p>
      <p class="contact__role">CEO</p>
      <p>TEL: 1300 4 52918</p>
      <p>FAX: 1300 5 52918</p>
      <p>Mobile: 0412 638194</p>
      <p>PO Box 917, Ferris Hollow, Brisbane, Qld 4127</p>
      <p>e: kylem@copperladder.com.au</p>
      <p>w: www.copperladder.com.au</p>
    </div>
  </section>

  <section class="card card--sky">
    <svg class="card__art" viewBox="0 0 432 250" preserveAspectRatio="none" aria-hidden="true">
      <defs>
        <linearGradient id="sky-bg" x1="0" y1="0" x2="1" y2="1">
          <stop offset="0" stop-color="var(--sky-light)"/>
          <stop offset="0.45" stop-color="var(--sky-mid)"/>
          <stop offset="1" stop-color="var(--sky)"/>
        </linearGradient>
        <linearGradient id="gold-fill-2" x1="0" y1="0" x2="1" y2="1">
          <stop offset="0" stop-color="var(--gold-light)"/>
          <stop offset="1" stop-color="var(--gold)"/>
        </linearGradient>
      </defs>
      <rect width="432" height="250" fill="url(#sky-bg)"/>
      <path d="M55 0 C72 100 215 150 432 156 L432 0 Z" fill="var(--swoosh-white)"/>
      <path d="M89 0 C106 72 225 128 432 137 L432 0 Z" fill="url(#gold-fill-2)"/>
    </svg>
    <div class="brand">The Copper Ladder</div>
    <div class="contact">
      <p class="contact__name">Kyle Morrison</p>
      <p class="contact__role">CEO</p>
      <p>TEL: 1300 4 52918</p>
      <p>FAX: 1300 5 52918</p>
      <p>Mobile: 0412 638194</p>
      <p>PO Box 917, Ferris Hollow, Brisbane, Qld 4127</p>
      <p>e: kylem@copperladder.com.au</p>
      <p>w: www.copperladder.com.au</p>
    </div>
  </section>

  <section class="card card--mist">
    <svg class="card__art" viewBox="0 0 432 250" preserveAspectRatio="none" aria-hidden="true">
      <defs>
        <linearGradient id="mist-bg" x1="0" y1="0" x2="1" y2="1">
          <stop offset="0" stop-color="var(--mist-light)"/>
          <stop offset="1" stop-color="var(--mist)"/>
        </linearGradient>
        <linearGradient id="gold-fill-3" x1="0" y1="0" x2="1" y2="1">
          <stop offset="0" stop-color="var(--gold-light)"/>
          <stop offset="1" stop-color="var(--gold)"/>
        </linearGradient>
      </defs>
      <rect width="432" height="250" fill="url(#mist-bg)"/>
      <path d="M55 0 C72 100 215 150 432 156 L432 0 Z" fill="var(--swoosh-white)"/>
      <path d="M89 0 C106 72 225 128 432 137 L432 0 Z" fill="url(#gold-fill-3)"/>
    </svg>
    <div class="brand">The Copper Ladder</div>
    <div class="contact">
      <p class="contact__name">Kyle Morrison</p>
      <p class="contact__role">CEO</p>
      <p>TEL: 1300 4 52918</p>
      <p>FAX: 1300 5 52918</p>
      <p>Mobile: 0412 638194</p>
      <p>PO Box 917, Ferris Hollow, Brisbane, Qld 4127</p>
      <p>e: kylem@copperladder.com.au</p>
      <p>w: www.copperladder.com.au</p>
    </div>
  </section>

</main>
</body>
</html>
```